Web Design Project: Facility Management company

Hi! We need a new website.

Our current website: http://www.vireo-trade.ru/ and we don-t like it. =)
The structure of our company has changed and now we don't need "cleaning" and "engeneering" on this site.

We are facility management company in Russia. So we provide integrated service solutions specific to industrial services: maintenance, repair, etc. of engineering systems.
More services:
Energy planning
Automation
Audit
Statements with regulators
Video surveillance
Central heating
Security systems
Welding
Management of subcontractors
Electrical installation and service needs
Reception
Catering

Visitors:
* Managers in the field of commercial real estate
* Chief engineers
* TOP managers of large companies, malls, factories...
+ their subordinates
* Small% of applicants.

Here you can see some websites/patterns we liked:
http://www.kobalmire.ru/ (This is our competitor’s site, so our site shouldn’t be an exact copy))))
http://www.dwatqo.ru/
http://www.layoutfarrow.com/demo/24296.html
http://www.layoutfarrow.com/website-templates/10145.html

Style:
Light, hi-tech/minimalizm, the color palette should be based on the original site colors (Green + black + white). http://www.vireo-trade.ru/

Estimated sitemap:
1. Home
2. About Us
3. Company's policy
4. History + Achievements.
5. Certificates
6. Map of presence (Here you can use sample map in file "our projects")
7. Services
8. Portfolio
9. News or blog
10. Jobs
11. Contacts - with the feedback form (or the function "call to order")
12. English

Need a design pages: main page, page 404. The rest of the page could be created by general pattern.

Logo, navigation bar and contacts should be visible on all pages of a site.
Flash animation elements and buttons, etc. - not needed.

* We need to develop 3 websites, so we are looking for a long term cooperation.
Looking forward to your creativity =)

Must Have:
Clear, intuitive structure of web pages.
In the center - of pictures reflecting our main services (industrial theme). May be in rotation.
BUT! This banner (central picture) should not be a huge one =)
All relevant information should be visible at once without scrolling.

A possibility to place media files (presentations, video ...) and 2 banner links on the main page.

Font should be available in Cyrillic.
Updates

IMPORTANT!

Please notice that in thisdesign we don't need "cleaning" and "engeneering" on this site.

So don't use old block of 4pictures from our current website. We don't need it anymore. 

Thestructure of our company has changed and now we need some links (may be banners,may be something else) to our future cleaning website as well as engeneeringwebsite.
It should look like seperate (partner) companies, not like our sevices.

Regards, Vera.

Please don't forget that we need bilingual site.

So define language changing tool in your designs.

Industry/Entity Type

Industrial

```html
<!DOCTYPE html>
<html lang="en">
<head>
<meta charset="utf-8">
<title>Vireo Service — Engineering Systems</title>
<link href="https://fonts.googleapis.com/css2?family=Advent+Pro:wght@500;600;700&family=Arimo:wght@400;700&display=swap" rel="stylesheet">
<style>
:root{
  --green:#8db50f;
  --lime:#c9e234;
  --lime-dark:#a9c31c;
  --ink:#111;
  --grey-text:#555;
  --topbar:#f1f1f1;
  --dark:#262626;
  --darker:#1d1d1d;
  --white:#fff;
  --display:'Advent Pro',sans-serif;
  --body:'Arimo',Arial,sans-serif;
}
*{margin:0;padding:0;box-sizing:border-box}
html,body{width:1200px;height:859px;overflow:hidden;background:var(--white)}
.page{position:relative;width:1200px;height:859px;font-family:var(--display);color:var(--grey-text)}
.abs{position:absolute}

.topbar{left:0;top:0;width:1200px;height:22px;background:var(--topbar);border-bottom:1px solid #e2e2e2}
.topbar a{position:absolute;top:4px;font-size:13px;font-weight:600;color:#666;text-decoration:none;text-transform:uppercase}
.topbar .sep{position:absolute;top:5px;width:1px;height:13px;background:#bbb}

.logo{left:169px;top:40px;display:flex;align-items:center;gap:10px}
.logo .mark{width:26px;height:26px;background:var(--lime)}
.logo .name{font-size:30px;font-weight:600;color:#222;letter-spacing:1px;line-height:1}
.logo .tag{font-size:12px;font-weight:500;color:#222;letter-spacing:1px}

.search{left:503px;top:48px;width:293px;height:23px;border:1px solid #bbb;background:#fff}
.search span{position:absolute;left:8px;top:2px;font-size:15px;color:#aaa;font-weight:600}
.search b{position:absolute;right:2px;top:2px;width:36px;height:17px;background:linear-gradient(#555,#111);color:#fff;font-size:13px;text-align:center;line-height:17px}

.lang{top:50px;font-size:13px;font-weight:600;color:#555;display:flex;align-items:center;gap:6px}
.lang i{display:block;width:20px;height:11px}

.nav{left:161px;top:117px;display:flex;font-size:13px;font-weight:600;color:#555;text-transform:uppercase;white-space:nowrap}
.nav span{padding:0 11px}
.nav span:first-child{padding-left:0}
.nav em{font-style:normal;color:#888}

.phone{left:816px;top:87px;font-size:25px;font-weight:600;color:var(--green);white-space:nowrap}
.email{left:818px;top:112px;font-size:17px;font-weight:600;color:#444;white-space:nowrap}
.contact-icon{left:979px;top:87px}

.hero{left:0;top:143px;width:1200px;height:209px;background:linear-gradient(180deg,#d2e83c,#bcd62a)}
.hero h1{position:absolute;left:157px;top:27px;font-size:64px;font-weight:600;line-height:54px;color:var(--ink);letter-spacing:1px}
.hero p{position:absolute;left:160px;top:148px;font-family:var(--body);font-size:12px;line-height:19px;color:#333;white-space:nowrap}
.hero .portrait{position:absolute;left:778px;top:2px;width:253px;height:207px;background:linear-gradient(180deg,#d9d2c7 0%,#9aa4b2 50%,#1c1f27 100%);border-radius:110px 110px 0 0}

.services{left:0;top:352px;width:1200px;height:196px;background:radial-gradient(ellipse 520px 120px at 420px 0,#6a6a6a,var(--dark) 80%)}
.card{position:absolute;top:34px;width:206px;height:117px}
.card .face{position:absolute;inset:0;transform:skewX(-7deg);border-radius:8px;border:2px solid rgba(255,255,255,.5)}
.card h3{position:absolute;left:22px;top:28px;font-size:26px;font-weight:700;line-height:22px;text-transform:uppercase}
.card .btn{position:absolute;left:2px;top:105px;width:148px;height:32px;background:linear-gradient(#555,#151515);border:1px solid #777;transform:skewX(-7deg);border-radius:4px;color:#eee;font-size:13px;font-weight:700;padding:7px 0 0 18px}
.card .btn i{position:absolute;right:14px;top:8px;width:15px;height:15px;border-radius:50%;border:2px solid}
.arrow{position:absolute;top:85px}

.lower{left:0;top:548px;width:1200px;height:255px;background:var(--darker);border-top:1px solid #555}
.lower h2{position:absolute;top:36px;font-size:22px;font-weight:600;color:var(--white);text-transform:uppercase}
.lower .hint{position:absolute;left:160px;top:63px;font-family:var(--body);font-size:11px;font-weight:700;color:#fff}
.map{position:absolute;left:169px;top:84px;width:225px;height:151px;background:linear-gradient(160deg,#a6d25a,#86bd3c)}
.video{position:absolute;left:443px;top:59px;width:278px;height:174px;border:4px solid #9a9a9a;background:linear-gradient(#56667a,#2f3540 60%,#1a1a1a)}
.video .bar{position:absolute;left:0;right:0;bottom:0;height:12px;background:#222}
.video .play{position:absolute;left:126px;top:66px}
.partner{position:absolute;left:780px;width:262px;height:66px;background:linear-gradient(#fff,#e1e1e1);border-bottom:3px solid #bbb;display:flex;align-items:center;padding-left:20px;gap:14px}
.partner i{width:24px;height:24px;background:var(--lime)}
.partner span{font-size:21px;font-weight:700;line-height:19px;color:#222;text-transform:uppercase}

.footer{left:0;top:803px;width:1200px;height:56px;background:var(--white)}
.footer .copy{position:absolute;left:161px;top:24px;font-family:var(--body);font-size:11px;color:#333}
.footer .copy b{font-weight:400;color:var(--green)}
.share{position:absolute;top:20px;height:15px;border:1px solid #bbb;font-family:var(--body);font-size:10px;color:#333;display:flex}
.share span{background:#e9eef5;padding:0 4px;border-right:1px solid #bbb}
.share em{font-style:normal;padding:0 4px}
.social-label{position:absolute;left:896px;top:22px;font-family:var(--body);font-size:10px;color:#3a78c3}
.social{position:absolute;top:19px;width:19px;height:19px;border-radius:3px}
</style>
</head>
<body>
<div class="page">

  <div class="abs topbar">
    <a style="left:722px">Portfolio</a><i class="sep" style="left:798px"></i>
    <a style="left:817px">News or Blog</a><i class="sep" style="left:914px"></i>
    <a style="left:933px">Jobs</a><i class="sep" style="left:974px"></i>
    <a style="left:992px">Service</a>
  </div>

  <div class="abs logo">
    <i class="mark"></i>
    <div><div class="name">VIREO SERVICE</div><div class="tag">engineering systems</div></div>
  </div>

  <div class="abs search"><span>SEARCH..</span><b>GO</b></div>

  <div class="abs lang" style="left:882px"><i style="background:linear-gradient(#c8102e 0 50%,#fff 50%)"></i>ENGLISH</div>
  <div class="abs lang" style="left:960px;color:#555">|</div>
  <div class="abs lang" style="left:974px"><i style="background:linear-gradient(#fff 0 33%,#0039a6 33% 66%,#d52b1e 66%)"></i>RUSSIA</div>

  <nav class="abs nav">
    <span>Home</span><em>|</em><span>About Us</span><em>|</em><span>Company's Policy</span><em>|</em><span>History &amp; Achievements.</span><em>|</em><span>Certificates</span><em>|</em><span>Map of Presence</span>
  </nav>

  <div class="abs phone">+7812 555 0148</div>
  <div class="abs email">info@vireoservice.com</div>
  <svg class="abs contact-icon" width="62" height="64" viewBox="0 0 62 64" aria-label="Contact">
    <rect x="1" y="1" width="60" height="50" rx="8" fill="#3a3a3a"/>
    <path d="M22 50 L31 62 L40 50 Z" fill="#3a3a3a"/>
    <rect x="16" y="22" width="30" height="20" rx="2" fill="#fff"/>
    <path d="M16 23 L31 34 L46 23" stroke="#3a3a3a" stroke-width="2" fill="none"/>
    <path d="M20 10 q11 -7 22 0" stroke="#9c9" stroke-width="4" fill="none"/>
  </svg>

  <section class="abs hero">
    <h1>DELENIT AUGUE<br>FEUGAIT NULLA</h1>
    <p>Lorem ipsum dolor sit amet, consectetur adipiscing elit. Nullam lorem dolor,<br>tristique in tincidunt in,suscipit sit amet felis. Sed placerat dictum libero, in sucipit</p>
    <div class="portrait" role="img" aria-label="Photo of a company engineer in a suit holding a hard hat"></div>
  </section>

  <section class="abs services">
    <svg class="arrow" style="left:161px" width="18" height="16"><path d="M17 0 L0 8 L17 16 L11 8 Z" fill="var(--lime)"/></svg>
    <svg class="arrow" style="left:1024px" width="18" height="16"><path d="M1 0 L18 8 L1 16 L7 8 Z" fill="var(--lime)"/></svg>

    <div class="card" style="left:186px">
      <div class="face" role="img" aria-label="Energy planning illustration with a light bulb" style="background:linear-gradient(135deg,#6ef0d0,#1fc49c)"></div>
      <h3 style="color:#f2e41b">Energy<br><span style="color:#fff;font-size:22px">Planning</span></h3>
      <div class="btn">VIEW SERVICE<i style="border-color:#5fd9d0"></i></div>
    </div>
    <div class="card" style="left:397px">
      <div class="face" role="img" aria-label="Video surveillance illustration with a running figure" style="background:linear-gradient(135deg,#f08a4a,#e0521c)"></div>
      <h3 style="color:#fff;left:80px;top:8px">Video</h3>
      <div class="btn">VIEW SERVICE<i style="border-color:#f06a2a"></i></div>
    </div>
    <div class="card" style="left:606px">
      <div class="face" role="img" aria-label="Security systems illustration with a shield and tick" style="background:linear-gradient(135deg,#f9d43a,#f0a80c)"></div>
      <h3 style="color:#222;font-size:24px;top:40px">Security<br><span style="color:#fff;font-size:18px">Systems</span></h3>
      <div class="btn">VIEW SERVICE<i style="border-color:#f3b81a"></i></div>
    </div>
    <div class="card" style="left:816px">
      <div class="face" role="img" aria-label="Central heating illustration with a house in a knitted hat" style="background:linear-gradient(135deg,#7cc4f5,#3b94df)"></div>
      <h3 style="color:#fff;left:86px;top:26px;font-size:23px">Central<br><span style="color:#e8321c">Heating</span></h3>
      <div class="btn">VIEW SERVICE<i style="border-color:#4aa3e8"></i></div>
    </div>
  </section>

  <section class="abs lower">
    <h2 style="left:157px">Our Location</h2>
    <div class="hint">Click map To Zoom In Our Location</div>
    <div class="map" role="img" aria-label="Map of company presence across Russia"></div>

    <h2 style="left:440px">Our Video</h2>
    <div class="video" role="img" aria-label="Video still of engineers in hard hats at a construction site">
      <svg class="play" width="42" height="42"><circle cx="21" cy="21" r="19" fill="rgba(0,0,0,.4)" stroke="#fff" stroke-width="2"/><path d="M16 12 L30 21 L16 30 Z" fill="#fff"/></svg>
      <div class="bar"></div>
    </div>

    <h2 style="left:780px">Our Partner Website</h2>
    <div class="partner" style="top:73px"><i></i><span>Vireo Cleaning<br>Service</span></div>
    <div class="partner" style="top:157px"><i></i><span>Vireo Engineering<br>Systems</span></div>
  </section>

  <footer class="abs footer">
    <div class="copy">© Copyright 2012 <b>Vireo Service</b> &nbsp;All rights reserved.</div>
    <div class="share" style="left:741px"><span>Share</span><em>8</em></div>
    <div class="share" style="left:822px"><span>Like</span><em>14</em></div>
    <div class="social-label">Social networks:</div>
    <i class="social" style="left:976px;background:#3b5998"></i>
    <i class="social" style="left:1000px;background:#55acee"></i>
    <i class="social" style="left:1024px;background:#00aff0"></i>
  </footer>

</div>
</body>
</html>
```